email presentation and marketing

we need a email to be used to present our company and services to potential customer. it needs to contain our logo, address, details about our company, photos and a well described text about our work .
I will send a web site from one of the company we are targeting.
The e mail must be sober, elegant, persuasive. The client needs to have the feeling it is dealing to a big company.
See below one of out potential clients
http://qorbelresidences.com/

Target Market(s)

High end custom homes

Industry/Entity Type

Painting And Decorating

Font styles to use
Serif
Sans Serif

Requirements
Must have
• Our name, location, portfolio (need to send some pics), web site http://kd-brushworks.com.
• Need to develop a email to present our company to potential clients.
Nice to have
• clients reviews.
• we are listed on nest rater. https://nestrater.net/firms/5813064-kd-bespoke?service_area=7640153
Should not have
• not colorful

```html
<!DOCTYPE html>
<html lang="en">
<head>
<meta charset="utf-8">
<title>KD Brushworks – Custom Home Painting</title>
<link rel="stylesheet" href="https://fonts.googleapis.com/css2?family=Lato:ital,wght@0,400;0,700;1,400&family=Roboto:wght@400;500;700&display=swap">
<style>
  :root {
    --ink-dark: #2b2c30;
    --ink-darker: #242528;
    --ink-deepest: #1c1d1f;
    --brand-yellow: #e3c616;
    --paper: #ffffff;
    --paper-soft: #efefef;
    --text-body: #2a2a2a;
    --text-muted: #6a6a6a;
    --text-light: #ffffff;
  }
  * { box-sizing: border-box; margin: 0; padding: 0; }
  html, body { width: 1200px; height: 3041px; overflow: hidden; }
  body {
    background: var(--ink-dark);
    font-family: "Lato", Arial, sans-serif;
    color: var(--text-body);
    position: relative;
  }
  .section { position: absolute; left: 0; width: 1200px; }

  /* Header */
  .header { top: 0; height: 298px; background: var(--ink-dark); }
  .brand-name {
    position: absolute; font-family: "Roboto", Arial, sans-serif; font-weight: 700;
    color: var(--brand-yellow); letter-spacing: 2px; text-align: center;
  }
  .header .brand-name { left: 230px; top: 112px; width: 300px; font-size: 40px; }
  .brand-square {
    position: absolute; background: var(--brand-yellow);
  }
  .header .brand-square { left: 362px; top: 58px; width: 36px; height: 36px; }
  .contact {
    position: absolute; right: 230px; top: 40px; text-align: right;
    font-family: "Roboto", Arial, sans-serif; color: var(--brand-yellow);
  }
  .contact .phone { font-size: 24px; font-weight: 500; margin-bottom: 38px; }
  .contact p { font-size: 17px; line-height: 22px; }
  .contact .gap { margin-top: 18px; }

  /* Hero */
  .hero { top: 298px; height: 1034px; background: var(--ink-dark); }
  .hero-photo {
    position: absolute; left: 34px; top: 0; width: 1134px; height: 628px;
    background: linear-gradient(180deg, #8d9298 0%, #b8bcc1 35%, #7f7c77 60%, #e9ecef 82%, #f5f6f7 100%);
  }
  .hero-edge {
    position: absolute; top: -4px; height: 576px; width: 34px;
    background: linear-gradient(180deg, #55585c, #3a3b3f);
  }
  .hero-edge.left { left: 0; }
  .hero-edge.right { right: 0; }
  .intro-title {
    position: absolute; left: 223px; top: 578px; width: 756px; height: 50px;
    background: var(--brand-yellow); text-align: center;
    font-family: "Roboto", Arial, sans-serif; font-weight: 700; font-size: 27px;
    line-height: 50px; color: var(--ink-darker);
  }
  .intro-card {
    position: absolute; left: 223px; top: 628px; width: 756px; height: 321px;
    background: var(--paper); border-radius: 0 0 16px 16px;
  }
  .intro-text {
    position: absolute; left: 30px; top: 28px; width: 450px;
    font-size: 19px; line-height: 32px; color: var(--text-body);
  }
  .intro-divider {
    position: absolute; left: 503px; top: 20px; width: 1px; height: 270px; background: #e2e2e2;
  }
  .service-list {
    position: absolute; left: 522px; top: 25px; width: 210px; list-style: none;
    font-family: "Roboto", Arial, sans-serif; font-weight: 700; font-size: 17px;
    line-height: 24px; color: var(--ink-darker);
  }
  .service-list li { margin-bottom: 32px; }
  .service-list li:first-child { margin-bottom: 8px; }
  .quote-button {
    position: absolute; left: 444px; width: 312px; height: 47px;
    background: var(--brand-yellow); border-radius: 24px; text-align: center;
    font-family: "Roboto", Arial, sans-serif; font-weight: 500; font-size: 24px;
    line-height: 47px; color: var(--ink-darker);
  }
  .hero .quote-button { top: 973px; }

  /* Testimonials */
  .testimonials { top: 1332px; height: 762px; background: var(--paper-soft); }
  .section-title {
    position: absolute; left: 0; width: 1200px; text-align: center;
    font-family: "Roboto", Arial, sans-serif; font-weight: 500; font-size: 31px;
  }
  .testimonials .section-title { top: 32px; color: #1f1f1f; }
  .review { position: absolute; top: 104px; width: 380px; text-align: center; }
  .review.first { left: 222px; }
  .review.second { left: 599px; }
  .review svg { display: block; margin: 0 auto; }
  .review-name {
    margin-top: 16px; font-family: "Roboto", Arial, sans-serif; font-size: 20px; color: #444;
  }
  .review-name.italic { font-style: italic; }
  .review-job { margin-top: 28px; font-family: "Roboto", Arial, sans-serif; font-size: 16px; color: #555; }
  .review-text {
    margin: 28px auto 0; width: 370px; font-style: italic; font-size: 15px;
    line-height: 20px; color: var(--text-muted);
  }
  .review-photo {
    position: absolute; top: 393px; width: 349px; height: 345px;
  }
  .review-photo.bedroom { left: 237px; background: linear-gradient(160deg, #cfcdcb 0%, #8f8c8a 45%, #3b3a3b 80%, #ececec 100%); }
  .review-photo.living { left: 616px; background: linear-gradient(180deg, #e9e6e3 0%, #cfc9c3 45%, #2a2a2b 60%, #bfb7ad 100%); }

  /* Our works */
  .works { top: 2094px; height: 464px; background: var(--ink-dark); }
  .works .section-title { top: 24px; color: var(--text-light); font-weight: 700; font-size: 27px; }
  .work-thumb { position: absolute; top: 101px; width: 144px; height: 237px; }
  .work-thumb.t1 { left: 245px; background: linear-gradient(180deg, #dcdcd8, #a5a8a3 60%, #e8e8e6); }
  .work-thumb.t2 { left: 434px; background: linear-gradient(180deg, #e2e2e2, #3a3a3a 55%, #d8d8d8); }
  .work-thumb.t3 { left: 622px; background: linear-gradient(180deg, #c4bdb1, #6a5a4a 55%, #3b2b22); }
  .work-thumb.t4 { left: 813px; background: linear-gradient(180deg, #8d8781, #b8aea3 45%, #4a4540 70%, #f1f1f1); }
  .works .quote-button { top: 385px; }

  /* Footer */
  .footer { top: 2558px; height: 412px; background: var(--ink-darker); text-align: center; }
  .footer .brand-square { left: 582px; top: 36px; width: 36px; height: 36px; }
  .footer .brand-name { left: 400px; top: 84px; width: 400px; font-size: 30px; }
  .footer-info {
    position: absolute; left: 0; top: 162px; width: 1200px;
    font-family: "Roboto", Arial, sans-serif; font-size: 20px; line-height: 26px; color: var(--text-light);
  }
  .social { position: absolute; left: 0; top: 330px; width: 1200px; display: flex; justify-content: center; gap: 17px; }
  .social span { width: 48px; height: 48px; border: 2px solid #9a9a9a; border-radius: 50%; }
  .legal {
    top: 2970px; height: 71px; background: var(--ink-deepest); text-align: center;
    font-family: "Roboto", Arial, sans-serif; font-size: 20px; line-height: 71px; color: var(--text-light);
  }
</style>
</head>
<body>

<header class="section header">
  <div class="brand-square"></div>
  <div class="brand-name">KD BRUSHWORKS</div>
  <div class="contact">
    <div class="phone">Ph: 416 555 0187</div>
    <p>A: 142 Maple Crest Rd, Unit C2 &nbsp;|&nbsp; L4K 2P9</p>
    <p>Toronto | Ontario</p>
    <p class="gap">info@kdbrushworksstudio.com</p>
    <p>http://kdbrushworksstudio.com/</p>
  </div>
</header>

<section class="section hero">
  <div class="hero-edge left"></div>
  <div class="hero-edge right"></div>
  <div class="hero-photo" role="img" aria-label="Large stone custom home with a turret, covered in winter snow"></div>
  <h1 class="intro-title">KD BRUSHWORKS – WE ARE ALWAYS READY TO SERVE</h1>
  <div class="intro-card">
    <p class="intro-text">KD Brushworks is a Toronto based company that provides customised home painting, commercial and industrial painting services to Greater Toronto and metropolitan cities. We use modern equipment and superior brand materials to deliver a high-quality work which makes us nothing less then proud.</p>
    <div class="intro-divider"></div>
    <ul class="service-list">
      <li>- WALLPAPER INSTALLATION</li>
      <li>- SPRAY FINISH</li>
      <li>- DRYWALL REPAIRS</li>
      <li>- STAIRCASE FINISH</li>
    </ul>
  </div>
  <div class="quote-button">GET A QUOTE</div>
</section>

<section class="section testimonials">
  <h2 class="section-title">CLIENT TESTIMONIALS</h2>
  <div class="review first">
    <svg width="74" height="74" viewBox="0 0 74 74" aria-hidden="true">
      <circle cx="37" cy="37" r="36" fill="#111"/>
      <circle cx="37" cy="28" r="11" fill="#fff"/>
      <path d="M16 58 a21 16 0 0 1 42 0 z" fill="#fff"/>
    </svg>
    <div class="review-name italic">TOMAS</div>
    <div class="review-job">Paint Of &nbsp;New Homes and Renovations</div>
    <p class="review-text">Kieran and his staff are reliable, provide great quality and service. myself and my clients are extremely satisfied with his work.</p>
  </div>
  <div class="review second">
    <svg width="74" height="74" viewBox="0 0 74 74" aria-hidden="true">
      <circle cx="37" cy="37" r="36" fill="#111"/>
      <circle cx="37" cy="28" r="11" fill="#fff"/>
      <path d="M16 58 a21 16 0 0 1 42 0 z" fill="#fff"/>
    </svg>
    <div class="review-name">Brelcon Build</div>
    <div class="review-job">Painting Of New Home</div>
    <p class="review-text">Contractor was hired to paint New home. Staff was friendly, courteous, helpful, clean, proactive, reliable.</p>
  </div>
  <div class="review-photo bedroom" role="img" aria-label="Finished bedroom with a patterned feature wallpaper wall"></div>
  <div class="review-photo living" role="img" aria-label="Freshly painted living room with fireplace and tall black-framed windows"></div>
</section>

<section class="section works">
  <h2 class="section-title">OUR WORKS</h2>
  <div class="work-thumb t1" role="img" aria-label="Bright bathroom with freestanding tub under arched windows"></div>
  <div class="work-thumb t2" role="img" aria-label="Curved staircase with dark finished treads and railing"></div>
  <div class="work-thumb t3" role="img" aria-label="Hallway with painted walls and dark hardwood floor"></div>
  <div class="work-thumb t4" role="img" aria-label="Living area with stone fireplace and built-in shelving"></div>
  <div class="quote-button">GET A QUOTE</div>
</section>

<footer class="section footer">
  <div class="brand-square"></div>
  <div class="brand-name">KD BRUSHWORKS</div>
  <div class="footer-info">
    <p>KD Brushworks</p>
    <p>Contact: Kieran Doyle</p>
    <p>416 555 0187|kdbrushworks.office@mailbox.com</p>
    <p>kd-brushworks.com</p>
  </div>
  <div class="social" aria-label="Social links">
    <span></span><span></span><span></span><span></span><span></span>
  </div>
</footer>

<div class="section legal">KD Brushworks © All rights reserved</div>

</body>
</html>
```